Bourbon Tasting Placemat

We are going to be hosting a Cedar and Fiddle night at Casa Nogal Asador and we need a flyer / place mat on which to put the 5 different American Whiskeys that will be tasted. The event will be both cultural and educational in addition to culinary and musical and should have design cues that help communicate the Southern Culture, music key aspects of American Whiskey and Casa Nogal positioning as an expert in that space. Please see attached files for design cues and information to be considered in the design.

The original designs can be in English and then in the revision process we can provide the Spanish translations as all info needs to be in Spanish for the final version.

Target Market(s)

Middle to Upper class Mexicans looking to learn about American Whiskeys (bourbon, rye, moonshine, Tennessee Whiskey)

Industry/Entity Type

Event

Requirements
Must have
• Place for 5 different types of American Whiskeys (see ppt example)
Notes section
Casa Nogal branding
Cultural, educational design cues (key info, images, history, etc)

```html
<!DOCTYPE html>
<html lang="es">
<head>
<meta charset="utf-8">
<title>Cedar &amp; Fiddle — Casa Nogal Asador</title>
<link href="https://fonts.googleapis.com/css2?family=Oswald:wght@400;500;600&family=Roboto+Condensed:wght@400;700&family=Playfair+Display:ital@1&display=swap" rel="stylesheet">
<style>
  :root {
    --page: #ffffff;
    --board: #141414;
    --board-edge: #0a0a0a;
    --band: #2a2a2a;
    --rule: #cfcfcf;
    --cream: #f3e58c;
    --white: #f4f4f4;
    --grey: #8a8a8a;
    --card: #e5e5e7;
    --ink: #111111;
    --img-dark: #3a3a3a;
    --img-mid: #6b6b6b;
  }
  * { box-sizing: border-box; margin: 0; padding: 0; }
  html, body { width: 1200px; height: 900px; overflow: hidden; background: var(--page); }
  .placemat {
    position: relative; width: 1200px; height: 900px;
    background: var(--page);
    font-family: "Roboto Condensed", Arial, sans-serif;
  }
  .board {
    position: absolute; left: 30px; top: 8px; width: 1140px; height: 884px;
    background: radial-gradient(ellipse at 50% 45%, #1d1d1d 0%, var(--board) 60%, var(--board-edge) 100%);
  }
  .band {
    position: absolute; left: 30px; width: 1140px; height: 14px;
    background: var(--band);
    border-top: 1px solid var(--grey); border-bottom: 1px solid var(--grey);
  }
  .band--top { top: 8px; }
  .band--bottom { bottom: 8px; }
  .frame {
    position: absolute; left: 62px; top: 42px; width: 1076px; height: 818px;
    border: 1px solid var(--rule);
  }
  .brand {
    position: absolute; top: 80px; width: 148px; height: 80px;
    display: flex; flex-direction: column; align-items: center; justify-content: center; gap: 5px;
    font-family: "Oswald", sans-serif; font-weight: 500; color: var(--white);
    text-transform: uppercase; text-align: center; line-height: 1;
  }
  .brand--left { left: 94px; }
  .brand--right { left: 958px; }
  .brand__dot { width: 12px; height: 12px; border-radius: 50%; background: var(--white); }
  .brand__name { font-size: 28px; letter-spacing: 1px; }
  .brand__sub { font-size: 17px; letter-spacing: 2px; }
  .title-rule { position: absolute; left: 272px; width: 654px; height: 1px; background: var(--rule); }
  .title-rule--top { top: 70px; }
  .title-rule--bottom { top: 165px; }
  .title {
    position: absolute; left: 272px; top: 74px; width: 654px; height: 88px;
    display: flex; align-items: center; justify-content: center; gap: 18px;
    font-family: "Oswald", sans-serif; font-weight: 600; font-size: 62px; line-height: 1;
    text-transform: uppercase;
  }
  .title__first { color: var(--cream); }
  .title__amp { font-family: "Playfair Display", serif; font-style: italic; font-weight: 400; font-size: 66px; color: var(--grey); }
  .title__second { color: var(--white); text-shadow: 3px 3px 0 #555; }
  .column { position: absolute; top: 185px; width: 190px; }
  .column--1 { left: 86px; } .column--2 { left: 295px; } .column--3 { left: 504px; }
  .column--4 { left: 713px; } .column--5 { left: 923px; }
  .medallion {
    width: 188px; height: 188px; border-radius: 50%;
    border: 4px dotted var(--white); padding: 5px; margin: 0 auto;
  }
  .medallion__inner {
    width: 100%; height: 100%; border-radius: 50%; border: 2px solid var(--white);
    background: var(--board); overflow: hidden;
    display: flex; flex-direction: column; align-items: center; justify-content: center;
    text-align: center; color: var(--white); font-size: 10px; line-height: 1.3; padding: 0 20px;
  }
  .medallion__inner b { color: var(--cream); font-weight: 700; text-transform: uppercase; }
  .fact-big { font-family: "Oswald", sans-serif; font-size: 18px; font-weight: 500; color: var(--cream); line-height: 1.15; }
  .visual { border-radius: 4px; margin-bottom: 6px; flex: none; }
  .visual--map { width: 96px; height: 44px; background: var(--img-mid); }
  .visual--tree { width: 90px; height: 60px; border-radius: 45px 45px 8px 8px; background: var(--img-mid); }
  .visual--flag { width: 92px; height: 40px; background: linear-gradient(var(--img-mid), #9a9a9a); }
  .visual--globe { width: 62px; height: 62px; border-radius: 50%; background: radial-gradient(circle at 40% 40%, #777, var(--img-dark)); margin-bottom: 4px; }
  .medallion__inner--photo { padding: 0; background: linear-gradient(160deg, #bdbdbd, #6e6e6e 55%, #3f3f3f); }
  .column__heading {
    margin-top: 20px; height: 50px;
    font-family: "Oswald", sans-serif; font-weight: 500; font-size: 21px; line-height: 1.15;
    color: var(--cream); text-align: center; text-transform: uppercase;
  }
  .column__rule { width: 150px; height: 1px; background: var(--grey); margin: 6px auto 10px; }
  .column__body { color: var(--white); font-size: 7.7px; line-height: 1.3; text-align: center; height: 236px; overflow: hidden; }
  .column__body p + p { margin-top: 8px; }
  .notes {
    position: absolute; top: 703px; width: 173px; height: 125px;
    background: var(--card); color: var(--ink); padding: 6px 8px;
    font-weight: 700; font-size: 9.5px; line-height: 1.45; text-transform: uppercase;
  }
  .notes__line { display: inline-block; width: 100px; border-bottom: 1px solid var(--ink); margin-left: 3px; }
  .notes--1 { left: 95px; } .notes--2 { left: 304px; } .notes--3 { left: 513px; }
  .notes--4 { left: 722px; } .notes--5 { left: 932px; }
</style>
</head>
<body>
<main class="placemat">
  <div class="board"></div>
  <div class="band band--top"></div>
  <div class="band band--bottom"></div>
  <div class="frame"></div>

  <div class="brand brand--left"><span class="brand__dot"></span><span class="brand__name">Casa Nogal</span><span class="brand__sub">Asador</span></div>
  <div class="brand brand--right"><span class="brand__dot"></span><span class="brand__name">Casa Nogal</span><span class="brand__sub">Asador</span></div>

  <div class="title-rule title-rule--top"></div>
  <h1 class="title"><span class="title__first">Cedar</span><span class="title__amp">&amp;</span><span class="title__second">Fiddle</span></h1>
  <div class="title-rule title-rule--bottom"></div>

  <section class="column column--1">
    <div class="medallion"><div class="medallion__inner">
      <div class="visual visual--map" role="img" aria-label="Mapa de Estados Unidos con Kentucky marcado"></div>
      <p>95% del <b>bourbon</b> esta hecho en <b>Kentucky</b>, pero técnicamente puede ser hecho en cualquier parte de EEUU.</p>
    </div></div>
    <h2 class="column__heading">Straight Kentucky<br>Bourbon</h2>
    <div class="column__rule"></div>
    <div class="column__body">
      <p>El bourbon es una bebida destilada de la familia de los whiskeys, se caracteriza por ser ligeramente aromático y de sabor acaramelado. El bourbon whiskey, según la ley estadounidense, debe ser elaborado a base de maíz por lo menos en una concentración entre el 50% y el 70%.</p>
      <p>Otros ingredientes añadidos son: el trigo, centeno y cebada. Su periodo de envejecimiento debe ser como mínimo de dos años, no existen requerimientos legales para este periodo mínimo y que el producto final se denomine "bourbon" pero sí existen requerimientos para denominarlo straight bourbon. Por regla general el bourbon se madura durante un periodo de 5 años en barricas de roble que pueden ser nuevas y/o tostadas.</p>
      <p>El nombre de la bebida destilada proviene del lugar de Estado Unidos donde se produce de manera originaria, Bourbon County (Kentucky), que a su vez, toma su nombre de la familia real de la Casa de Borbón.</p>
    </div>
  </section>

  <section class="column column--2">
    <div class="medallion"><div class="medallion__inner">
      <div class="visual visual--tree" role="img" aria-label="Silueta de un roble"></div>
      <p>El bourbon debe añejarse en <b>barricas nuevas de roble americano.</b></p>
    </div></div>
    <h2 class="column__heading">Tennessee<br>Whiskey</h2>
    <div class="column__rule"></div>
    <div class="column__body">
      <p>El Tennessee Whiskey es un straight bourbon, lo que obliga a envejecer el destilado un mínimo de 2 años dentro de la barrica. Por lo demás, las normas de producción son las mismas que las del bourbon de Kentucky con dos excepciones:</p>
      <p>La primera, que para denominarse Tennessee Whiskey si es obligatorio que se haya producido, destilado y embotellado en el estado de Tennessee. La segunda, que antes de introducir el whiskey en la barrica para su añejamiento, éste es filtrado a través de una columna de 3 metros de carbón vegetal de madera de arce. De esta forma adquiere un aroma más suave y sabor más dulce que el bourbon de Kentucky.</p>
      <p>Los barriles de whisky se fabrican con roble blanco de América debido a que esta madera tiene la combinación necesaria de compuestos para lograr el producto final. Mientras el whisky se añeja dentro del barril, la madera se contrae y expande según los cambios climáticos que se produzcan en su entorno.</p>
    </div>
  </section>

  <section class="column column--3">
    <div class="medallion"><div class="medallion__inner">
      <div class="visual visual--flag" role="img" aria-label="Bandera de Estados Unidos"></div>
      <p class="fact-big">EN MAYO DE 1964</p>
      <p>el congreso de EEUU, reconoce al Bourbon como un <b>"producto distintivo de EEUU"</b>.</p>
    </div></div>
    <h2 class="column__heading">American Rye<br>Whiskey</h2>
    <div class="column__rule"></div>
    <div class="column__body">
      <p>El método de destilación es prácticamente igual al del bourbon, y la gente suele confundirlos. La diferencia más notable es que el American Rye Whiskey debe ser elaborado de cebada por lo menos en un 51% de la composición total.</p>
      <p>En 1700's y 1800's el Rye Whiskey era el whiskey preferido en los estados del noroeste de los Estado Unidos, incluyendo Pensilvania y Maryland. Jacob Harlan, el primer presidente de su condado, hacía Rye Whiskey en su hacienda de Harlan Hill.</p>
      <p>Originalmente los principales cócteles americanos como el: Old Fashioned, Manhattan y Whiskey Sours, se hacían de rye, pero con la introducción del bourbon en los estados del norte, se comenzó a cambiar el rye por el bourbon.</p>
      <p>El Rye es reconocido por sus sabores picantes y frutosos añadidos al whiskey. Mientras que el bourbon con su base mínima de 51% de maíz tiene un sabor mas dulce y con mas cuerpo. El rye es también mucho mas seco y se puede decir que es equivalente a un Islay whiskey o whiskey escoses.</p>
    </div>
  </section>

  <section class="column column--4">
    <div class="medallion"><div class="medallion__inner">
      <div class="visual visual--globe" role="img" aria-label="Globo terráqueo"></div>
      <p>Bourbon tiene el proceso de destilación</p>
      <p class="fact-big">MÁS REGULADO</p>
      <p>del <b>mundo.</b></p>
    </div></div>
    <h2 class="column__heading">Appalachian<br>Moonshine</h2>
    <div class="column__rule"></div>
    <div class="column__body">
      <p>Moonshine, white lightning, mountain dew, hooch, y Tennessee white whiskey son términos para describir alcoholes de alto grado que están destilado de manera ilegal. La palabra "moonshine" proviene de la palabra "moonrakers" que fue usado para describir a los contrabandistas (que trabajaban bajo la luz de la luna) y las operaciones clandestinas usadas por las destilerías ilegales en la zona de Apalachina en el sureste de Estados Unidos.</p>
      <p>El Moonshine es muy fuerte dado el hecho de que no se corta ni se madura. Cuando sale de la destilería en su ultimo proceso, es de color totalmente transparente y tiene entre 150 y 170 grados. Muchos dicen que en los viejos tiempos los contrabandistas lo utilizaban como gasolina y es por eso que las policías nunca los pudieron agarrar. Por otro lado el deporte de StockRace creció en el sur de los EEUU por algo.</p>
    </div>
  </section>

  <section class="column column--5">
    <div class="medallion"><div class="medallion__inner medallion__inner--photo" role="img" aria-label="Fotografía antigua en blanco y negro de una banda de bluegrass al aire libre"></div></div>
    <h2 class="column__heading">Bluegrass<br>Music</h2>
    <div class="column__rule"></div>
    <div class="column__body">
      <p>Bluegrass music is a form of American roots music, and a sub-genre of country music. Bluegrass was inspired by the music of Appalachia. It has mixed roots in Irish, Scottish, Welsh, and English traditional music, and also later influenced by the music of African-Americans through incorporation of jazz elements.</p>
      <p>In bluegrass, as in some forms of jazz, one or more instruments each takes its turn playing the melody and improvising around it, while the others perform accompaniment. This is in contrast to old-time music, in which all instruments play the melody together or one instrument carries the lead throughout while the others provide accompaniment.</p>
      <p>Bluegrass music has attracted a diverse following worldwide. Bluegrass pioneer Walt Carver characterized the genre as: "Scottish bagpipes and ole-time fiddlin'. It's Methodist and Holiness and Baptist. It's blues and jazz, and it has a high lonesome sound."</p>
    </div>
  </section>

  <div class="notes notes--1">Nombre<span class="notes__line"></span><br>Notas:</div>
  <div class="notes notes--2">Nombre<span class="notes__line"></span><br>Notas:</div>
  <div class="notes notes--3">Nombre<span class="notes__line"></span><br>Notas:</div>
  <div class="notes notes--4">Nombre<span class="notes__line"></span><br>Notas:</div>
  <div class="notes notes--5">Nombre<span class="notes__line"></span><br>Notas:</div>
</main>
</body>
</html>
```